KestrelNet Business Cards

Create business cards for our exciting new software company. We provide cloud billing systems and provisioning software for campany that need monthly SaaS and Cloud Billing

Target Market(s)

Enterprise businesses, b2b, telecom carriers, software manufactures

Industry/Entity Type

Software

```html
<!DOCTYPE html>
<html lang="en">
<head>
<meta charset="utf-8">
<title>KestrelNet Business Cards</title>
<link rel="stylesheet" href="https://fonts.googleapis.com/css2?family=Tenor+Sans&display=swap">
<style>
  :root {
    --page: #ffffff;
    --card: #1c3553;
    --wave: #172e4a;
    --accent: #7fcdea;
    --faint: #162e4b;
  }
  * { margin: 0; padding: 0; box-sizing: border-box; }
  html, body {
    width: 1200px;
    height: 1000px;
    overflow: hidden;
    background: var(--page);
  }
  body { position: relative; font-family: "Tenor Sans", sans-serif; }

  .card {
    position: absolute;
    width: 575px;
    height: 340px;
    background: var(--card);
    box-shadow: 3px 3px 6px rgba(0, 0, 0, 0.35);
    overflow: hidden;
  }
  .card--front { left: 85px; top: 145px; }
  .card--back  { left: 515px; top: 577px; }

  .card__ornament {
    position: absolute;
    left: 0;
    width: 575px;
  }
  .card--front .card__ornament {
    top: 140px;
    height: 200px;
    background: linear-gradient(to bottom, rgba(23, 46, 74, 0) 0%, var(--wave) 100%);
  }
  .card--back .card__ornament {
    top: 140px;
    height: 200px;
    background: linear-gradient(to bottom, rgba(23, 46, 74, 0) 0%, var(--wave) 100%);
  }

  .brand-name {
    position: absolute;
    left: 0;
    width: 575px;
    top: 174px;
    text-align: center;
    font-size: 46px;
    line-height: 1;
    color: var(--accent);
    letter-spacing: 1px;
  }

  .brand-name--faint {
    left: auto;
    right: 26px;
    width: auto;
    top: 62px;
    font-size: 22px;
    color: var(--faint);
    letter-spacing: 0.5px;
  }

  .contact {
    position: absolute;
    left: 37px;
    top: 80px;
    color: var(--accent);
    font-variant: small-caps;
    letter-spacing: 1.4px;
    line-height: 1;
  }
  .contact__name    { font-size: 14px; }
  .contact__role    { font-size: 11px; margin-top: 1px; }
  .contact__address { margin-top: 34px; font-size: 13px; line-height: 15px; text-transform: lowercase; }
  .contact__phone   { margin-top: 26px; font-size: 14px; }
  .contact__email   { font-size: 13px; margin-top: 2px; text-transform: lowercase; }
  .contact__web     { font-size: 13px; margin-top: 18px; text-transform: lowercase; }
</style>
</head>
<body>

  <section class="card card--front">
    <div class="card__ornament" role="img" aria-label="Flowing multi-line wave ornament across the lower card"></div>
    <div class="brand-name">KestrelNet</div>
  </section>

  <section class="card card--back">
    <div class="card__ornament" role="img" aria-label="Flowing multi-line wave ornament across the lower card"></div>
    <div class="brand-name brand-name--faint">KestrelNet</div>

    <div class="contact">
      <p class="contact__name">Mara Quinlan</p>
      <p class="contact__role">Marketing</p>
      <p class="contact__address">Address line - Address line<br>Address line - Address line</p>
      <p class="contact__phone">Phone: (000) 000-0000</p>
      <p class="contact__email">Email: quinlan@kestrelnet.com</p>
      <p class="contact__web">www.kestrelnet.com</p>
    </div>
  </section>

</body>
</html>
```